creative design for packing box of 3D paper puzzle

We want to get a packaging box design for the 3D puzzle. The packaging is for animal puzzles, like birds, insect ,wild animal. it is for young chirdren. 5-12 years old.
The box size : 12*17*2CM, 2.5CM header. Attach is some packing design ideal and our logo.
We like more nice design. It can attract the eyes. We hope all items can be use same background, and just change the color and put different animal photo on it. Box is same design, you can check the file “box-different color” . same design, just diffirent color, photo, text..
Please send us your design in diffirent color. Also You can visit our website: www.tovel.com. you can kow how about our product.
We attach 3 items photo. You can choose one to make the designon. Our product is DIY, education. Animal with scene
Target Market(s)
Europe,Janpan,USA
Colors
Designer to choose colors to be used in the design.
Requirements
Must have
- our Logo, some nice text or signo
Nice to have
- nice background

```html
<!DOCTYPE html>
<html lang="en">
<head>
<meta charset="utf-8">
<title>TOVEL 3D Paper Puzzle – Box Dieline</title>
<link href="https://fonts.googleapis.com/css2?family=Lilita+One&family=Fredoka:wght@600&display=swap" rel="stylesheet">
<style>
  :root {
    --purple: #a55ffd;
    --cyan: #4bd9f9;
    --sand: #f0c96e;
    --royal: #1437e6;
    --navy: #1c3f73;
    --grape: #7a1a8c;
    --white: #ffffff;
    --paper: #fdfafc;
    --grey: #a0a0a0;
    --cut: #e02020;
  }
  html, body { margin: 0; padding: 0; overflow: hidden; background: var(--white); }
  .canvas { width: 1200px; height: 1200px; position: relative; }
  .canvas svg { display: block; }
  .title { font-family: "Lilita One", sans-serif; }
  .title--plain { fill: var(--white); font-size: 58px; }
  .title--outlined { fill: var(--white); stroke: var(--royal); stroke-width: 8px; paint-order: stroke; stroke-linejoin: round; font-size: 58px; }
  .title--side { font-size: 61px; }
  .title--bar { fill: var(--white); font-size: 56px; }
  .notice { font-family: "Fredoka", sans-serif; font-weight: 600; fill: var(--grey); font-size: 24px; }
  .age { font-family: "Lilita One", sans-serif; fill: var(--grape); font-size: 29px; }
  .brand { font-family: "Fredoka", sans-serif; font-weight: 600; fill: var(--navy); }
  .brand--large { font-size: 40px; letter-spacing: 3px; }
  .brand--small { font-size: 11px; }
  .dieline { fill: none; stroke: var(--cut); stroke-width: 1; }
</style>
</head>
<body>
<div class="canvas">
<svg width="1200" height="1200" viewBox="0 0 1200 1200" xmlns="http://www.w3.org/2000/svg">

  <!-- background art -->
  <g class="background-art" role="img" aria-label="Playful abstract background of purple, sand and cyan blobs with dotted and wavy patterns">
    <rect x="33" y="193" width="1149" height="937" fill="var(--purple)"/>
    <path d="M33 430 Q120 420 200 470 L330 560 L560 640 L420 1000 L380 1130 L33 1130 Z" fill="var(--cyan)"/>
    <path d="M560 193 L1020 193 Q1030 300 1090 330 Q1182 360 1182 420 L1182 600 Q1080 660 1060 680 Q1000 700 960 660 Q900 580 780 600 Q700 610 650 560 Q590 500 600 400 Q620 320 560 250 Z" fill="var(--sand)"/>
    <path d="M810 620 Q900 560 980 640 Q1050 700 1100 640 Q1150 600 1182 610 L1182 1130 L780 1130 Q760 900 790 760 Z" fill="var(--cyan)"/>
    <path d="M690 640 Q760 590 810 620 L790 760 Q760 900 780 1130 L510 1130 Q480 1000 520 880 Q560 800 620 760 Q660 700 690 640 Z" fill="var(--purple)"/>
    <ellipse cx="1005" cy="955" rx="35" ry="42" fill="var(--sand)"/>
    <circle cx="410" cy="1090" r="32" fill="none" stroke="var(--white)" stroke-width="14"/>
  </g>

  <!-- top header -->
  <text class="title title--plain" x="343" y="322" text-anchor="middle">3D PAPER PUZZLE</text>

  <!-- product window (drawn beneath the title bar) -->
  <circle cx="340" cy="590" r="212" fill="var(--paper)" stroke="var(--royal)" stroke-width="11"/>
  <text class="notice" x="362" y="558" text-anchor="middle">CLEAR AREA</text>
  <text class="notice" x="362" y="583" text-anchor="middle">TO SHOW PRODUCT</text>

  <!-- front panel title bar -->
  <rect x="118" y="360" width="457" height="50" fill="var(--royal)"/>
  <text class="title title--bar" x="345" y="405" text-anchor="middle">3D PAPER PUZZLE</text>

  <!-- age badge -->
  <circle cx="238" cy="893" r="68" fill="var(--white)" stroke="var(--royal)" stroke-width="10"/>
  <text class="age" x="240" y="882" text-anchor="middle">5 TO 12</text>
  <text class="age" x="240" y="908" text-anchor="middle">YEARS</text>
  <text class="age" x="240" y="934" text-anchor="middle">OLD</text>

  <!-- brand badge -->
  <circle cx="425" cy="840" r="100" fill="var(--white)" stroke="var(--royal)" stroke-width="12"/>
  <text class="brand brand--large" x="425" y="855" text-anchor="middle">TOVEL</text>

  <!-- side panel titles -->
  <text class="title title--outlined title--side" transform="translate(57 658) rotate(90)" text-anchor="middle">3D PAPER PUZZLE</text>
  <text class="title title--outlined title--side" transform="translate(594 658) rotate(90)" text-anchor="middle">3D PAPER PUZZLE</text>

  <!-- side panel small brand badges -->
  <g class="side-badges">
    <circle cx="75" cy="378" r="28" fill="var(--white)" stroke="var(--royal)" stroke-width="5"/>
    <text class="brand brand--small" x="75" y="382" text-anchor="middle">TOVEL</text>
    <circle cx="75" cy="937" r="28" fill="var(--white)" stroke="var(--royal)" stroke-width="5"/>
    <text class="brand brand--small" x="75" y="941" text-anchor="middle">TOVEL</text>
    <circle cx="613" cy="380" r="28" fill="var(--white)" stroke="var(--royal)" stroke-width="5"/>
    <text class="brand brand--small" x="613" y="384" text-anchor="middle">TOVEL</text>
    <circle cx="612" cy="937" r="28" fill="var(--white)" stroke="var(--royal)" stroke-width="5"/>
    <text class="brand brand--small" x="612" y="941" text-anchor="middle">TOVEL</text>
  </g>

  <!-- bottom flap title -->
  <text class="title title--outlined" transform="translate(345 1004) rotate(180)" text-anchor="middle">3D PAPER PUZZLE</text>

  <!-- cutting dieline -->
  <g class="dieline">
    <path d="M118 1118 L118 240 Q118 205 150 205 L540 205 Q575 205 575 240 L575 1118 Q575 1120 540 1120 L150 1120 Q118 1120 118 1090"/>
    <path d="M40 337 L40 262 L70 258 L620 258 L650 262 L650 337"/>
    <line x1="40" y1="337" x2="1160" y2="337"/>
    <line x1="40" y1="337" x2="40" y2="1050"/>
    <line x1="40" y1="985" x2="1160" y2="985"/>
    <path d="M40 1050 L70 1062 L620 1062 L650 1050"/>
    <line x1="578" y1="337" x2="578" y2="985"/>
    <line x1="650" y1="240" x2="650" y2="1050"/>
    <path d="M652 240 L652 150 Q652 108 700 108 L1060 108 Q1110 108 1110 150 L1110 985"/>
    <line x1="652" y1="240" x2="1110" y2="240"/>
    <path d="M838 183 L930 183 Q940 190 930 197 L838 197 Q824 205 824 195 Q824 183 838 183 Z"/>
    <path d="M838 270 L930 270 Q940 283 930 297 L838 297 Q824 297 824 283 Q824 270 838 270 Z"/>
    <path d="M1110 337 L1160 350 L1160 975 L1110 985"/>
  </g>
</svg>
</div>
</body>
</html>
```